Buch-/eBook-Cover für einen Elternratgeber
Zielgruppe
Buch: Elternratgeber
Titel: Taler begreifen
Untertitel: Deiner Tochter den klugen Blick vermitteln
Wir sind der Sulbe Verlag und suchen ein passendes Cover für unseren neuen Elternratgeber. Mit diesem Buch möchten wir Eltern unterstützen, ihren Kindern einen guten und verantwortungsvollen Umgang mit Geld zu vermitteln.
Anforderungen an das Cover-Design:
Bitte keinen Comicstil
Das Buch richtet sich an Eltern (nicht kindlich oder verspielt gestalten)
Keine direkte Darstellung von Geld (z. B. keine Münzen, Geldscheine, Sparschweine usw.)
Ob mit oder ohne Personen auf dem Cover: sind wir offen
Farbwahl und Bildsprache: gerne seriös, ansprechend und modern
Wir sind gespannt auf kreative und professionelle Vorschläge!
E-Book E-Book"
Das Design darf nicht zu überladen sein.

```html
<!DOCTYPE html>
<html lang="de">
<head>
<meta charset="utf-8">
<title>Taler begreifen – Buchcover</title>
<link rel="stylesheet" href="https://fonts.googleapis.com/css2?family=Outfit:wght@400;500&display=swap">
<style>
  :root {
    --stage: #ecebe7;
    --paper: #fcf3e3;
    --ink: #2f4a46;
    --ink-soft: #4a6b63;
    --sage: #a9c0b2;
    --sage-light: #d7e2d6;
    --band: #4f7d6a;
    --band-text: #f6efe0;
    --accent: #e8685c;
    --accent-text: #fff5ef;
    --tab: #ffffff;
  }
  * { margin: 0; padding: 0; box-sizing: border-box; }
  html, body {
    width: 1200px; height: 900px; overflow: hidden;
    background: var(--stage);
    font-family: "Outfit", sans-serif;
  }
  .book-cover {
    position: absolute;
    left: 367px; top: 75px;
    width: 466px; height: 748px;
    background: var(--paper);
    box-shadow: 0 8px 24px rgba(0,0,0,0.15);
    overflow: hidden;
  }
  .author {
    position: absolute; left: 32px; top: 32px;
    font-size: 15px; font-weight: 400; color: var(--ink-soft);
    letter-spacing: 0.3px;
  }
  .badge {
    position: absolute; left: 339px; top: 24px;
    width: 104px; height: 104px; border-radius: 50%;
    background: var(--accent); color: var(--accent-text);
    display: flex; align-items: center; justify-content: center;
    text-align: center; font-size: 15px; line-height: 1.3;
  }
  .title {
    position: absolute; left: 30px; top: 138px;
    font-size: 78px; font-weight: 500; line-height: 84px;
    color: var(--ink); letter-spacing: -0.5px;
  }
  .subtitle {
    position: absolute; left: 32px; top: 310px; width: 410px;
    font-size: 24px; font-weight: 500; line-height: 31px;
    color: var(--ink);
  }
  .cover-illustration {
    position: absolute; left: 0; top: 414px;
    width: 466px; height: 230px;
    background: linear-gradient(180deg, var(--paper) 0%, var(--sage-light) 45%, var(--sage) 100%);
  }
  .bottom-band {
    position: absolute; left: 0; top: 644px;
    width: 466px; height: 104px;
    background: var(--band);
  }
  .tagline {
    position: absolute; left: 32px; top: 20px;
    font-size: 18px; color: var(--band-text);
  }
  .publisher-tab {
    position: absolute; right: 0; top: 10px;
    width: 42px; height: 94px;
    background: var(--tab); border-radius: 6px 0 0 0;
    display: flex; align-items: center; justify-content: center;
  }
  .publisher-tab span {
    writing-mode: vertical-rl;
    font-size: 14px; font-weight: 500; color: var(--accent);
  }
</style>
</head>
<body>
  <div class="book-cover">
    <p class="author">Lena Maurer</p>
    <div class="badge">Mit<br>Übungen</div>
    <h1 class="title">Taler<br>begreifen</h1>
    <p class="subtitle">Deiner Tochter den klugen Blick vermitteln.</p>
    <div class="cover-illustration" role="img" aria-label="Illustration: goldene Münzen mit Sparschwein vor sanften grünen Hügeln"></div>
    <div class="bottom-band">
      <p class="tagline">Ein Praxisbuch für Familien</p>
      <div class="publisher-tab"><span>Sulbe</span></div>
    </div>
  </div>
</body>
</html>
```